Create modern and sleek business card for luxury real estate company

We're a "boutique" real estate office looking for a design that gets across a highly modern luxury brand. Blacks and whites are probably the best colors unless we try a silver foil for the logo. I've attached a version of our current logo here. I'd like to swap out the current font on there with Gotham Light Regular.

I'm looking to have one side of the card have the logo with the space for our agents info on the other side.

Target Market(s)

Young professionals in a "luxury" headspace

Industry/Entity Type

Real estate

Contact Information for Business Card

A place for agent name, cell number, website. The slogan "Simply Rethinking Real Estate".

Font styles to use
Other font styles liked:
• Gotham Regular

Colors

Designer to choose only greyscale colors for use in the design.

Requirements
Must have
• Matte black as the background color. Clean lines and use of contrast. A specific design aspect that will use silver foil.
Nice to have
• Up in the air on integrating a QR code
Should not have
• Any houses or other real estate related design (ex: a clip art house)

```html
<!DOCTYPE html>
<html lang="en">
<head>
<meta charset="utf-8">
<title>Halden Realty – Business Card</title>
<link href="https://fonts.googleapis.com/css2?family=Montserrat:wght@300;400;600&display=swap" rel="stylesheet">
<style>
  :root {
    --stage: #1c1c1d;
    --card: #262526;
    --card-edge: #2e2d2e;
    --white: #f4f4f4;
    --silver: #bdbdbd;
    --grey: #9a9a9a;
    --emboss: #343334;
    --pattern-dark: #232223;
    --pattern-light: #3a393a;
  }
  * { box-sizing: border-box; margin: 0; padding: 0; }
  html, body {
    width: 1200px; height: 1200px; overflow: hidden;
    background: var(--stage);
    font-family: "Montserrat", "Helvetica Neue", Arial, sans-serif;
  }
  .stage {
    position: relative; width: 1200px; height: 1200px;
    display: flex; flex-direction: column; align-items: center; justify-content: center; gap: 40px;
  }
  .card {
    position: relative; width: 900px; height: 514px;
    background: var(--card); overflow: hidden;
    box-shadow: 0 14px 30px rgba(0,0,0,.45);
    border: 1px solid var(--card-edge);
  }
  .card__pattern {
    position: absolute; inset: 0;
    background: linear-gradient(110deg, var(--pattern-dark) 0%, var(--card) 50%, var(--pattern-light) 100%);
  }
  .lockup {
    position: absolute; display: flex; align-items: center; gap: 22px;
  }
  .lockup__circle {
    width: 110px; height: 110px; border-radius: 50%;
    border: 2px solid var(--white); flex: none;
  }
  .lockup__divider { width: 1px; height: 100px; background: var(--grey); }
  .lockup__name {
    color: var(--white); font-weight: 300; font-size: 40px;
    line-height: 1; letter-spacing: .12em; text-transform: uppercase;
  }
  .card--back .lockup { right: 70px; bottom: 110px; }
  .card--back .lockup__circle, .card--back .lockup__name { border-color: var(--silver); color: var(--silver); }

  .card--front .lockup { left: 70px; top: 60px; }
  .agent { position: absolute; left: 70px; top: 250px; }
  .agent__name {
    color: var(--white); font-weight: 600; font-size: 30px; letter-spacing: .24em; text-transform: uppercase;
  }
  .agent__title {
    color: var(--grey); font-weight: 400; font-size: 22px; letter-spacing: .22em; text-transform: uppercase; margin-top: 6px;
  }
  .contact { list-style: none; margin-top: 22px; color: var(--silver); font-weight: 400; font-size: 23px; letter-spacing: .14em; }
  .contact li { margin-bottom: 12px; }
  .emboss-circle {
    position: absolute; right: -150px; top: 150px; width: 480px; height: 480px;
    border-radius: 50%; border: 2px solid var(--emboss);
  }
</style>
</head>
<body>
<main class="stage">
  <section class="card card--back">
    <div class="card__pattern" role="img" aria-label="Tone-on-tone repeating brand pattern with silver foil fade"></div>
    <div class="lockup">
      <span class="lockup__circle"></span>
      <span class="lockup__divider"></span>
      <span class="lockup__name">Halden<br>Realty</span>
    </div>
  </section>

  <section class="card card--front">
    <span class="emboss-circle" aria-hidden="true"></span>
    <div class="lockup">
      <span class="lockup__circle"></span>
      <span class="lockup__divider"></span>
      <span class="lockup__name">Halden<br>Realty</span>
    </div>
    <div class="agent">
      <h1 class="agent__name">Agent Name Here</h1>
      <p class="agent__title">Realtor</p>
      <ul class="contact">
        <li>tel : 1234-1234-123</li>
        <li>mail : info@haldenrealty.com</li>
        <li>web : haldenrealty.com</li>
      </ul>
    </div>
  </section>
</main>
</body>
</html>
```